Attorney Recruiting company needs brochure

Brief Harbor is a company that recruits attorneys for law firms and corporations. We want a brochure that makes the law firms and corporation want to retain us to recruit attorneys when they are hiring. We identify experienced well qualified attorneys. We provide them for direct hire (also knows as permanent placement) and for temporary contract hourly work. We want our colors included: red, black and white. It has to convey professionalism and experience. You can find lots of information about who we are and what we do on our website. www.briefharbor-example.com. The brochure should be in traditional conservative font. Should be easy to read. Attorneys tend to scan brochures to see what we do, they will need read it word for word, so we don't need lots of paragraphs and extraneous text. The brochure should outline easily the services we provide which are very specific. They are outlined on home page of website. You should also include our logo which I will attach in several formats.

Target Market(s)

Attorneys and executives

Industry/Entity Type

Conservative

Requirements
Must have
• logo
colors described above

```html
<!DOCTYPE html>
<html lang="en">
<head>
<meta charset="utf-8">
<title>Brief Harbor – Attorney Recruiting</title>
<link rel="stylesheet" href="https://fonts.googleapis.com/css2?family=Arimo:wght@400;500;600&display=swap">
<style>
  :root {
    --page-bg: #2c2d31;
    --tile: #333439;
    --tile-soft: #303135;
    --text-white: #f4f4f4;
    --text-soft: #e6e6e6;
    --accent-red: #c8202f;
  }
  html, body {
    margin: 0;
    padding: 0;
    width: 1200px;
    height: 848px;
    overflow: hidden;
    background: var(--page-bg);
  }
  .brochure-page {
    position: relative;
    width: 1200px;
    height: 848px;
    background: var(--page-bg);
    overflow: hidden;
    font-family: "Arimo", Arial, sans-serif;
    color: var(--text-white);
  }
  .backdrop {
    position: absolute;
    inset: 0;
  }
  .headline {
    position: absolute;
    left: 96px;
    top: 104px;
    margin: 0;
    font-size: 25px;
    font-weight: 500;
    line-height: 33px;
    letter-spacing: 0.4px;
    text-transform: uppercase;
  }
  .offer-list {
    position: absolute;
    left: 96px;
    top: 244px;
    width: 640px;
    margin: 0;
    padding: 0;
    list-style: none;
    font-size: 15.5px;
    line-height: 20px;
    letter-spacing: 0.3px;
    text-transform: uppercase;
    color: var(--text-soft);
  }
  .offer-list li {
    position: relative;
    padding-left: 26px;
    margin-bottom: 8.5px;
  }
  .offer-list li::before {
    content: "";
    position: absolute;
    left: 1px;
    top: 7px;
    width: 5px;
    height: 5px;
    background: var(--accent-red);
  }
  .section-title {
    position: absolute;
    left: 96px;
    top: 452px;
    margin: 0;
    font-size: 25px;
    font-weight: 500;
    letter-spacing: 0.4px;
    text-transform: uppercase;
  }
  .services-copy {
    position: absolute;
    left: 96px;
    top: 564px;
    width: 700px;
    margin: 0;
    font-size: 15.5px;
    line-height: 21.5px;
    letter-spacing: 0.3px;
    text-transform: uppercase;
    color: var(--text-soft);
  }
</style>
</head>
<body>
  <main class="brochure-page">
    <svg class="backdrop" width="1200" height="848" viewBox="0 0 1200 848" aria-hidden="true">
      <rect x="313" y="0" width="314" height="107" fill="var(--tile)"/>
      <rect x="0" y="107" width="88" height="236" fill="var(--tile-soft)"/>
      <rect x="1104" y="107" width="96" height="236" fill="var(--tile)"/>
      <rect x="898" y="614" width="302" height="234" fill="var(--tile)"/>
    </svg>

    <h1 class="headline">We secure top legal talent for<br>positions with top employers, including:</h1>

    <ul class="offer-list">
      <li>Direct hire for permanent positions</li>
      <li>Hourly/contract work for temporary positions</li>
      <li>Temporary to permanent positions</li>
      <li>Litigation and transactional positions</li>
      <li>Law firm associate, partner and in-house legal counsel positions</li>
    </ul>

    <h2 class="section-title">Our Services</h2>

    <p class="services-copy">We recruit qualified attorneys for placement with law firms and companies to handle litigation or transactional legal work. We provide attorneys for direct hire, temporary projects and temporary-to-hire. We work on practice group mergers for some of our law firm clients. We work on a contingency fee or retained search basis.</p>
  </main>
</body>
</html>
```